Tuition Center Website

We need a new web site for a tutoring company based in sydney.

We only teach senior highschool students and pride ourselves on building the students abilities to think their way through life.

I would like a bright and vibrant website that looks professional and modern.
It needs to look simple and neat but also have the functionality we need.
Images and flash would be good.

Please keep in mind that the site must be appealing to a younger audience.

We need a multipage website with the following navigation bars:

1.Home (As logo not "home" button)
I would like a news box/ticker somewhere that can stream our chatterbook and peeplr feeds and also any news updates we want to put up.
Subscribe to newsletter button.

2. About us.
This needs to be a pull down into:
-What we do
-Why we do it
-How we do it

3. Courses
Pulldown into:
-Maths
-English
-Science
(we may need to attach extra pages behind these e.g. Courses/Science/Physics or Courses/Science/Chemistry and possibly add a link to a new formvik form)

4. Inspired
This page is like a blog page where we can upload videos, links to articles that we find to be inspiring and hopefully will inspire others.

5. Inspire
This is a recruitment page. Only content here.

6. Contact us.
Trovix map widget and a 'contact us' form

* Our branding requires green close to #12FF3D

***Please have a look at the current website.
@ www.velmoralearning.com.au

Thanks everybody hope the revision of my brief is better and more informative than my last one
Updates

Target Market(s)

senior highschool students aged 15-19, parents ( to a lesser degree)

Industry/Entity Type

It Company

Requirements
Must have
• Ability to change content on pages.

The green doesn't have to be everywhere, but it must be obvious that it is our colour.

Nice to have
• Sites with a nicer mix of images and flash will be given more consideration. But then again, if you amaze us, you amaze us and we will go with your design.
Should not have
• Should stay away from ocre, brown colours and serif fonts.

```html
<!DOCTYPE html>
<html lang="en">
<head>
<meta charset="utf-8">
<title>velmora learning | HSC tutoring &amp; mentoring</title>
<link rel="stylesheet" href="https://fonts.googleapis.com/css2?family=Andika:wght@400;700&family=Arimo:wght@400;700&display=swap">
<style>
:root{
  --green:#5fe000;
  --ink:#111;
  --text:#222;
  --grey-bg:#e6e6e6;
  --white:#fff;
  --footer:#0b1f2a;
  --footer-base:#061821;
  --muted:#c9d1d6;
  --link-blue:#1a5fb4;
  --bar-blue:#3b5998;
}
*{box-sizing:border-box;margin:0;padding:0}
html,body{width:994px;height:1200px;overflow:hidden}
body{position:relative;background:var(--white);font-family:"Arimo",Arial,sans-serif;color:var(--text)}
.abs{position:absolute}

/* header */
.brand{left:118px;top:14px;width:104px}
.brand-mark{width:82px;height:66px;background:var(--green);margin-left:10px}
.brand-name{font-family:"Andika",sans-serif;font-size:17px;line-height:16px;color:var(--ink);margin-top:5px;text-align:center;width:102px}
.tagline{left:305px;top:68px;font-family:"Andika",sans-serif;font-size:17px;color:var(--ink)}
.tagline em{font-style:normal;color:var(--green)}
.social{right:116px;top:8px;display:flex;gap:8px;font-family:"Andika",sans-serif;font-size:10px;color:#555}
.social span{display:flex;align-items:center;gap:3px}
.social i{width:10px;height:10px;background:#3a6ea5;display:inline-block}

/* navigation */
.main-nav{left:0;top:130px;width:994px;height:29px;background:var(--green)}
.main-nav a{position:absolute;top:4px;font-family:"Andika",sans-serif;font-size:14px;color:var(--white);text-decoration:none}
.dropdown{left:191px;top:159px;width:107px;height:70px;background:rgba(95,224,0,.75);padding:3px 0 0 9px;z-index:3}
.dropdown a{display:block;font-family:"Andika",sans-serif;font-size:12px;line-height:20px;color:var(--white);text-decoration:none}

/* hero */
.hero{left:0;top:159px;width:994px;height:264px;background:linear-gradient(90deg,#c9c4c2 0%,#d8cfcb 18%,#cdb9b3 38%,#d6d0cc 55%,#c7b2ab 72%,#d3ccc8 88%,#c4bdb9 100%)}
.hero-shade{left:460px;top:159px;width:420px;height:264px;background:linear-gradient(90deg,rgba(80,70,66,0),rgba(80,70,66,.28) 20%,rgba(80,70,66,.28) 85%,rgba(80,70,66,0))}
.hero-photo{left:125px;top:210px;width:320px;height:213px;background:linear-gradient(160deg,#e3b89a 0%,#d6566a 30%,#f0e6d8 50%,#4aa3c8 72%,#6fbf3a 100%);border-radius:60px 60px 0 0;opacity:.85}
.hero-title{left:476px;top:176px;font-family:"Andika",sans-serif;font-weight:700;font-size:36px;color:var(--green);text-shadow:1px 2px 2px rgba(0,0,0,.35)}
.hero-copy{left:475px;top:231px;width:392px;font-family:"Andika",sans-serif;font-size:15.6px;line-height:20.6px;color:var(--white);text-shadow:0 1px 2px rgba(0,0,0,.5)}
.btn{display:block;background:var(--green);color:#111;font-family:"Andika",sans-serif;font-size:12px;text-align:center;border:1px solid #d8ffc0;text-decoration:none}
.hero-btn{left:475px;top:387px;width:80px;height:20px;line-height:18px}

/* content */
.content{left:0;top:423px;width:994px;height:555px;background:var(--grey-bg)}
.card{background:var(--white);border-top:4px solid var(--green)}
.card h2{font-family:"Andika",sans-serif;font-weight:400;color:var(--ink)}
.welcome{left:113px;top:435px;width:529px;height:265px}
.welcome h2{position:absolute;left:14px;top:14px;font-size:22px}
.welcome p{position:absolute;left:14px;top:53px;width:233px;font-size:10.4px;line-height:13.4px;text-align:justify;color:#111}
.welcome-photo{left:265px;top:54px;width:247px;height:191px;background:linear-gradient(135deg,#36524a,#8fa18f 45%,#c9a06b 70%,#3a6bb0)}

.feed{left:654px;top:435px;width:227px;height:277px}
.phone{left:7px;top:4px;width:212px;height:260px;background:#fff;border:1px solid #ccc}
.phone-status{height:12px;background:#111;color:#fff;font-size:8px;display:flex;justify-content:space-between;padding:0 5px;line-height:12px}
.phone-top{height:28px;background:linear-gradient(#6d87bd,var(--bar-blue));position:relative}
.phone-top b{position:absolute;left:0;right:0;top:5px;text-align:center;color:#fff;font-size:15px}
.phone-top i{position:absolute;top:5px;width:26px;height:18px;border:1px solid #2b4379;border-radius:3px;background:#5572a8}
.phone-search{margin:4px 3px;height:20px;border:1px solid #aaa;border-radius:10px;font-size:9.5px;color:#999;padding:4px 8px;background:#fff}
.post{display:flex;gap:6px;padding:4px 4px;border-bottom:1px solid #ddd;height:51px;font-size:9px;line-height:10.5px;color:#111}
.post .av{width:20px;height:20px;background:#8b7566;flex:none}
.post .go{width:14px;height:14px;border-radius:50%;background:#2f6fd0;flex:none;align-self:center}
.phone-tabs{position:absolute;left:0;bottom:0;width:210px;height:33px;background:#222;display:flex}
.phone-tabs span{flex:1;color:#ccc;font-size:6px;text-align:center;padding-top:22px;position:relative}
.phone-tabs span::before{content:"";position:absolute;left:50%;top:5px;width:14px;height:13px;margin-left:-7px;background:#777;border-radius:2px}
.phone-tabs span.on{background:#444}
.phone-tabs span.on::before{background:#5a9be0}

.news{left:113px;top:710px;width:267px;height:256px}
.news h2{position:absolute;left:13px;top:10px;font-size:18px}
.news-item{position:absolute;left:14px;width:245px;height:60px}
.news-item .thumb{position:absolute;left:0;top:0;width:77px;height:58px;background:linear-gradient(#7fb3e6,#b9c9d8 60%,#8a7f6f)}
.news-item h3{position:absolute;left:83px;top:0;font-size:10.5px;color:var(--green);font-weight:700;white-space:nowrap}
.news-item .date{position:absolute;left:83px;top:14px;font-size:8px;color:#666}
.news-item p{position:absolute;left:83px;top:26px;width:150px;font-size:9px;line-height:10.6px;color:#222}

.say{left:397px;top:710px;width:245px;height:256px}
.say h2{position:absolute;left:15px;top:10px;font-size:17px}
.say p{position:absolute;left:15px;top:46px;width:212px;font-size:9.8px;line-height:15.8px;color:#111}
.say cite{position:absolute;left:15px;top:180px;font-style:normal;font-family:"Andika",sans-serif;font-size:12px;color:#111}

.tweets{left:654px;top:725px;width:227px;height:241px}
.tw-box{left:7px;top:11px;width:211px;height:220px;border:1px solid #ccc;border-radius:3px;background:#fff}
.tw-head{height:30px;background:#eee;padding:4px 7px;font-size:11px;font-weight:700;color:#222;position:relative}
.tw-head small{display:block;font-size:8px;font-weight:400;color:#555}
.tw-head small b{color:#4aa3df}
.tw-head .ctl{position:absolute;right:6px;top:4px;display:flex;gap:3px}
.tw-head .ctl i{width:9px;height:9px;border:1px solid #888;display:block;background:#fff}
.tw{display:flex;gap:6px;padding:4px 5px 0 7px;height:41px}
.tw .av{width:33px;height:32px;background:#7a6f66;flex:none}
.tw p{border:1px solid #4aa3df;background:#eef7fd;font-size:9.5px;line-height:11px;padding:1px 4px;color:#222;width:145px}
.tw p u{color:var(--link-blue)}
.tw-more{font-size:8.6px;color:var(--link-blue);text-decoration:underline;padding:7px 0 0 7px}
.tw-offer{border-top:1px solid #ddd;margin:6px 6px 0;padding-top:7px;font-size:7.6px;color:#222;font-weight:700}
.tw-offer span{display:block;font-weight:400;color:var(--link-blue);text-decoration:underline;padding-left:44px;font-size:8.4px}

/* footer */
.site-footer{left:0;top:978px;width:994px;height:198px;background:var(--footer)}
.footer-base{left:0;top:1176px;width:994px;height:24px;background:var(--footer-base);color:#aab4ba;font-family:"Andika",sans-serif;font-size:12px;text-align:center;line-height:22px}
.site-footer h4{position:absolute;font-family:"Andika",sans-serif;font-weight:400;font-size:13px;color:var(--muted)}
.site-footer ul{position:absolute;list-style:none;font-size:11px;line-height:19px;color:var(--white)}
.site-footer ul .sub{color:var(--green);padding-left:14px}
.divider{position:absolute;top:1004px;width:1px;height:160px;background:#1d3340}
.nl-input{left:397px;top:1021px;width:144px;height:20px;border:1px solid #5d6d76;background:#0e2530;color:#8c989e;font-size:10px;padding:3px 5px}
.nl-btn{left:397px;top:1059px;width:80px;height:19px;line-height:17px;border-color:#c9ff9c}
.foot-mark{left:654px;top:1009px;width:51px;height:38px;background:var(--green)}
.foot-name{left:654px;top:1049px;font-family:"Andika",sans-serif;font-size:12px;color:var(--white)}
.contact-lines{left:654px;top:1073px;font-size:11px;line-height:19px;color:var(--white)}
</style>
</head>
<body>

<header>
  <div class="abs brand">
    <div class="brand-mark"></div>
    <div class="brand-name">velmora learning</div>
  </div>
  <p class="abs tagline">inspiring minds <em>nurturing potential</em> equipping success</p>
  <div class="abs social">
    <span><i></i>chatterbook</span>
    <span><i></i>peeplr</span>
    <span><i></i>linkwork</span>
  </div>
</header>

<section class="abs hero" role="img" aria-label="Softly blurred library bookshelves"></section>
<div class="abs hero-shade"></div>
<div class="abs hero-photo" role="img" aria-label="Group of cheerful senior students giving thumbs up"></div>
<h1 class="abs hero-title">i am velmora.</h1>
<p class="abs hero-copy">real HSC coaching &amp; mentoring.<br>The HSC help you need, in the years you need it. We offer small classes, individualised attention and genuine care for each student. It's different - in a good way. Feel free to find out more about us, and let us know if there's any way we can help you on your journey.</p>
<a class="abs btn hero-btn" href="#">Enquiry Now</a>

<nav class="abs main-nav">
  <a href="#" style="left:131px">Home</a>
  <a href="#" style="left:201px">About us</a>
  <a href="#" style="left:291px">Courses</a>
  <a href="#" style="left:378px">Inspired</a>
  <a href="#" style="left:463px">Inspire</a>
  <a href="#" style="left:540px">Contact us</a>
</nav>
<div class="abs dropdown">
  <a href="#">-What we do</a>
  <a href="#">-Why we do it</a>
  <a href="#">-How we do it</a>
</div>

<main class="abs content"></main>

<section class="abs card welcome">
  <h2>Welcome to velmora learning</h2>
  <p>Lorem Ipsum. Proin gravida nibh vel velit auctor aliquet. Aenean sollicitudin, lorem quis bibendum auctor, nisi elit consequat ipsum, nec sagittis sem nibh id elit. Duis sed odio sit amet nibh vulputate cursus a sit amet mauris. Morbi accumsan ipsum velit. Nam nec tellus a odio tincidunt auctor a ornare odio. Sed non mauris vitae erat consequat auctor eu in elit. Class aptent taciti sociosqu ad litora torquent per conubia nostra, per inceptos himenaeos. Mauris in erat justo. Nullam ac urna eu felis dapibus condimentum sit ame a augue. Sed non neque elit. Sed ut imperdiet nisi. Proin condimentum fermentum nunc. Etiam pharetra, erat sed fermentum feugiat, velit mauris egestas</p>
  <div class="abs welcome-photo" role="img" aria-label="Smiling students with books in front of a chalkboard"></div>
</section>

<aside class="abs card feed">
  <div class="abs phone">
    <div class="phone-status"><span>Telvo</span><b>9:39 PM</b><span>▮▮</span></div>
    <div class="phone-top"><i style="left:4px"></i><b>chatterbook</b><i style="right:4px"></i></div>
    <div class="phone-search">What are you doing?</div>
    <div class="post"><i class="av"></i><div><b>Lorem Ipsum. Proin gravida</b><br>vel velit auctor aliquet. Aenean sollicitudin, lorem quis bibendum auctor, nisi elit consequat ipsum,</div><i class="go"></i></div>
    <div class="post"><i class="av"></i><div><b>Lorem Ipsum. Proin gravida</b><br>vel velit auctor aliquet. Aenean sollicitudin, lorem quis bibendum</div><i class="go"></i></div>
    <div class="post" style="border:0"><i class="av"></i><div><b>Lorem Ipsum. Proin gravida</b><br>vel velit auctor aliquet. Aenean sollicitudin, lorem quis bibendum</div><i class="go"></i></div>
    <div class="phone-tabs"><span class="on">Home</span><span>Profile</span><span>Friends</span><span>Chat</span><span>Inbox</span></div>
  </div>
</aside>

<section class="abs card news">
  <h2>Latest news</h2>
  <article class="news-item" style="top:44px"><div class="thumb" role="img" aria-label="Students jumping for joy"></div><h3>Lorem Ipsum proin gravida nibh</h3><span class="date">30 / 04 / 2013</span><p>Lorem Ipsum. Proin gravida nibh vel velit auctor aliquet. Aenean sollicitudin, lorem quis bibendum</p></article>
  <article class="news-item" style="top:114px"><div class="thumb" role="img" aria-label="Students jumping outdoors"></div><h3 style="left:85px">Lorem Ipsum proin gravida nibh</h3><span class="date" style="left:85px">30 / 04 / 2013</span><p style="left:85px">Lorem Ipsum. Proin gravida nibh vel velit auctor aliquet. Aenean sollicitudin, lorem quis bibendum</p></article>
  <article class="news-item" style="top:181px"><div class="thumb" role="img" aria-label="Students celebrating with arms raised"></div><h3 style="left:85px">Lorem Ipsum proin gravida nibh</h3><span class="date" style="left:85px">30 / 04 / 2013</span><p style="left:85px">Lorem Ipsum. Proin gravida nibh vel velit auctor aliquet. Aenean sollicitudin, lorem quis bibendum</p></article>
</section>

<section class="abs card say">
  <h2>What Our Students Say.</h2>
  <p>Lorem Ipsum. Proin gravida nibh vel velit auctor aliquet. Aenean sollicitudin, lorem quis bibendum auctor, nisi elit consequat ipsum, nec sagittis sem nibh id elit. Duis sed odio sit amet nibh vulputate cursus a sit amet mauris. Morbi accumsan ipsum velit. Nam nec tellus a odio tincidunt auctor a ornare odio. Sed non mauris vitae erat consequat auctor eu in elit.</p>
  <cite>~WH, Halden House</cite>
</section>

<aside class="abs card tweets">
  <div class="abs tw-box">
    <div class="tw-head">Tweets in New York<small>Powered by <b>peeplr</b></small><span class="ctl"><i></i><i></i><i></i></span></div>
    <div class="tw"><i class="av"></i><p><u>Lorem Ipsum</u>: vel velit auctor aliquet. Aenean sollicitudin, lorem quis bibendum auctor,</p></div>
    <div class="tw"><i class="av"></i><p><u>Lorem Ipsum</u>: vel velit auctor aliquet. Aenean sollicitudin, lorem quis bibendum auctor,</p></div>
    <div class="tw"><i class="av"></i><p><u>Lorem Ipsum</u>: vel velit auctor aliquet. Aenean sollicitudin, lorem quis bibendum auctor,</p></div>
    <div class="tw-more">» See More Tweets in New York on peeplr.com</div>
    <div class="tw-offer">Online Offers:<span>Wireless Deals in New York</span></div>
  </div>
</aside>

<footer class="abs site-footer">
  <h4 style="left:127px;top:8px">Sitemap</h4>
  <ul style="left:127px;top:26px">
    <li>Home</li><li>About us</li>
    <li class="sub">-What we do</li><li class="sub">-Why we do it</li><li class="sub">-How we do it</li>
    <li style="margin-top:3px;line-height:14px">Courses</li>
    <li class="sub">-Maths</li><li class="sub">-English</li><li class="sub">-Science</li>
  </ul>
  <ul style="left:240px;top:26px"><li>Inspired</li><li>Inspire</li><li>Contact us</li></ul>
  <h4 style="left:398px;top:8px">Sing Up For Newsletter</h4>
  <h4 style="left:653px;top:8px">Contact us</h4>
</footer>
<span class="divider" style="left:346px"></span>
<span class="divider" style="left:597px"></span>
<div class="abs nl-input">Enter Email Address</div>
<a class="abs btn nl-btn" href="#">Send</a>
<div class="abs foot-mark"></div>
<div class="abs foot-name">velmora learning</div>
<div class="abs contact-lines">Street: 48 Larkfield Rd Ashbury NSW 2193<br>Phone: (02) 5550 0142<br>Email: learn@velmoralearning.com.au</div>
<div class="abs footer-base">© 2013 velmora learning | HSC tutoring &amp; mentoring</div>

</body>
</html>
```